Torvane Facilities Business Card Design

We would now like to design business cards with the new Torvane Facilities logo

Target Market(s)

Professional

Industry/Entity Type

Professional services

Contact Information for Business Card

Employee name, title, phone number, email address, corporate office address and logo.

Font styles to use
Sans Serif

Colors
0054AA
0677BA
7BADD7
CADEEF
E8F1F8

Requirements
Must have
• My logo
Should not have
• any other pictures or images besides my logo

```html
<!DOCTYPE html>
<html lang="en">
<head>
<meta charset="utf-8">
<title>Torvane Facilities Business Card</title>
<link rel="stylesheet" href="https://fonts.googleapis.com/css2?family=Oswald:wght@500&family=Roboto:wght@400;500&display=swap">
<style>
  :root {
    --stage: #2b2b2b;
    --card-blue: #0781ea;
    --ink: #ffffff;
    --ink-soft: rgba(255,255,255,0.92);
  }
  * { box-sizing: border-box; margin: 0; padding: 0; }
  html, body {
    width: 1200px;
    height: 1015px;
    overflow: hidden;
    background: var(--stage);
  }
  .stage {
    width: 1200px;
    height: 1015px;
    display: flex;
    flex-direction: column;
    align-items: center;
    justify-content: center;
    gap: 48px;
  }
  .card {
    width: 735px;
    height: 420px;
    background: var(--card-blue);
    position: relative;
    color: var(--ink);
    font-family: "Roboto", Arial, sans-serif;
  }
  .card-front {
    display: flex;
    align-items: center;
    justify-content: center;
  }
  .brand-name {
    font-family: "Roboto", Arial, sans-serif;
    font-weight: 500;
    font-size: 46px;
    letter-spacing: 1px;
    color: var(--ink);
  }
  .card-back .contact {
    position: absolute;
    left: 70px;
    top: 150px;
  }
  .person-name {
    font-family: "Oswald", "Arial Narrow", sans-serif;
    font-weight: 500;
    font-size: 30px;
    line-height: 1.05;
    text-transform: uppercase;
    letter-spacing: -0.3px;
  }
  .person-title {
    font-size: 17px;
    margin-left: 14px;
    margin-bottom: 26px;
    color: var(--ink-soft);
  }
  .contact-list {
    list-style: none;
    margin-left: 42px;
    font-size: 17px;
    line-height: 25px;
  }
  .contact-list li {
    display: flex;
    align-items: center;
    gap: 8px;
  }
  .contact-list svg {
    width: 16px;
    height: 16px;
    flex: none;
  }
  .address {
    margin-left: 66px;
    margin-top: 26px;
    font-size: 17px;
    line-height: 25px;
    font-style: normal;
  }
</style>
</head>
<body>
<main class="stage">
  <section class="card card-front" aria-label="Business card front">
    <span class="brand-name">Torvane Facilities</span>
  </section>

  <section class="card card-back" aria-label="Business card back">
    <div class="contact">
      <h1 class="person-name">Elias Marrow</h1>
      <p class="person-title">Managing Director</p>
      <ul class="contact-list">
        <li>
          <svg viewBox="0 0 16 16" aria-hidden="true"><path fill="#fff" d="M3.6 1.5l2.3 2.3-1.3 1.6c.9 2 2.4 3.5 4.3 4.4l1.6-1.3 2.3 2.3-1.6 2c-5-.6-8.9-4.5-9.5-9.5z"/></svg>
          044-555 018 274
        </li>
        <li>
          <svg viewBox="0 0 16 16" aria-hidden="true"><rect x="1" y="3.5" width="14" height="9" fill="#fff"/><path d="M1 3.5l7 5 7-5" fill="none" stroke="#0781ea" stroke-width="1.2"/></svg>
          info@torvanefacilities.com
        </li>
        <li>
          <svg viewBox="0 0 16 16" aria-hidden="true"><g fill="none" stroke="#fff" stroke-width="1.3"><circle cx="8" cy="8" r="6.5"/><ellipse cx="8" cy="8" rx="2.8" ry="6.5"/><path d="M1.5 8h13M2.5 5h11M2.5 11h11"/></g></svg>
          www.torvanefacilities.com
        </li>
      </ul>
      <address class="address">18 Calder Row, Suite 4<br>60718, Northbridge</address>
    </div>
  </section>
</main>
</body>
</html>
```